Business Card Design

We are a residential half way house for the addict ,the alcoholic and dual diagnosed in recovery.
i house both men and woman age 18+

Industry/Entity Type

Residential

```html
<!DOCTYPE html>
<html lang="en">
<head>
<meta charset="utf-8">
<title>Margaret's Family Sober House – Business Card</title>
<link rel="stylesheet" href="https://fonts.googleapis.com/css2?family=Ubuntu:wght@400;500;700&display=swap">
<style>
  :root {
    --stage: #1e1a19;
    --card-white: #ffffff;
    --brand-blue: #2a63a9;
    --accent-orange: #f07c2a;
    --ink: #2b2b2b;
    --back-center: #5f82c3;
    --back-edge: #244d99;
    --photo-blue: #a9cbe8;
    --photo-light: #e6eff8;
  }
  * { margin: 0; padding: 0; box-sizing: border-box; }
  html, body { width: 1000px; height: 1200px; overflow: hidden; }
  body {
    position: relative;
    background: var(--stage);
    font-family: "Ubuntu", sans-serif;
  }
  .card {
    position: absolute;
    left: 139px;
    width: 723px;
    height: 423px;
    overflow: hidden;
  }
  .card-front { top: 139px; background: var(--card-white); }
  .card-back {
    top: 676px;
    background: radial-gradient(ellipse 60% 60% at 52% 42%, var(--back-center) 0%, var(--back-edge) 100%);
    color: var(--card-white);
    text-align: center;
  }

  .front-photo {
    position: absolute;
    left: 0; top: 0;
    width: 460px; height: 423px;
    background: linear-gradient(90deg, var(--photo-blue) 0%, var(--photo-light) 55%, rgba(255,255,255,0) 100%);
  }

  .front-info {
    position: absolute;
    right: 34px;
    top: 70px;
    width: 340px;
    text-align: right;
  }
  .brand-name {
    font-weight: 700;
    font-size: 36px;
    letter-spacing: 2.5px;
    line-height: 1;
    color: var(--brand-blue);
  }
  .brand-sub {
    font-size: 20px;
    color: var(--brand-blue);
    margin-top: 6px;
  }
  .person-name {
    font-weight: 500;
    font-size: 23px;
    color: var(--accent-orange);
    margin-top: 32px;
  }
  .person-role {
    font-size: 20px;
    color: var(--ink);
    margin-top: 2px;
  }
  .person-role small { font-size: 18px; }
  .divider {
    height: 2px;
    background: var(--brand-blue);
    margin: 9px 0 16px auto;
    width: 328px;
  }
  .contact {
    display: flex;
    justify-content: flex-end;
    align-items: center;
    gap: 6px;
    font-size: 18px;
    color: var(--ink);
    height: 24px;
    margin-bottom: 10px;
  }
  .contact-icon {
    width: 23px; height: 23px;
    background: var(--accent-orange);
    border-radius: 2px;
    display: flex; align-items: center; justify-content: center;
  }
  .tagline {
    font-size: 18px;
    color: var(--brand-blue);
    margin-top: 20px;
  }

  .back-content { position: absolute; left: 0; right: 0; top: 148px; }
  .back-content .brand-name { color: var(--card-white); }
  .back-content .brand-sub { color: var(--card-white); margin-top: 8px; }
  .back-tagline { font-size: 18px; margin-top: 14px; }
  .back-address { font-size: 18px; margin-top: 28px; }
  .heart-decor {
    position: absolute;
    left: 316px; top: 250px;
    width: 102px; height: 102px;
    border-radius: 50%;
    background: rgba(255,255,255,0.18);
  }
</style>
</head>
<body>

<section class="card card-front">
  <div class="front-photo" role="img" aria-label="Photo of a nurse in light blue scrubs with a stethoscope writing on a clipboard"></div>
  <div class="front-info">
    <div class="brand-name">MARGARET'S</div>
    <div class="brand-sub">FAMILY SOBER HOUSE INC.</div>
    <div class="person-name">DANA WHITFIELD</div>
    <div class="person-role">Owner <small>(15 yrs.in recovery)</small></div>
    <div class="divider"></div>
    <div class="contact">
      <span>(555) 010-0305 / (555) 010-0306</span>
      <span class="contact-icon">
        <svg width="14" height="14" viewBox="0 0 24 24"><path fill="#fff" d="M6.6 10.8a15 15 0 0 0 6.6 6.6l2.2-2.2a1 1 0 0 1 1-.25 11.4 11.4 0 0 0 3.6.57 1 1 0 0 1 1 1V20a1 1 0 0 1-1 1A17 17 0 0 1 3 4a1 1 0 0 1 1-1h3.5a1 1 0 0 1 1 1c0 1.25.2 2.45.57 3.57a1 1 0 0 1-.25 1z"/></svg>
      </span>
    </div>
    <div class="contact">
      <span>(555) 010-5536</span>
      <span class="contact-icon">
        <svg width="14" height="14" viewBox="0 0 24 24"><path fill="#fff" d="M6 2h9l3 3v5H6z M4 11h16a2 2 0 0 1 2 2v7a2 2 0 0 1-2 2H4a2 2 0 0 1-2-2v-7a2 2 0 0 1 2-2z"/><rect x="6" y="14" width="8" height="1.6" fill="#f07c2a"/><rect x="6" y="17" width="8" height="1.6" fill="#f07c2a"/></svg>
      </span>
    </div>
    <div class="contact">
      <span>danawhitfield@mailbox.com</span>
      <span class="contact-icon">
        <svg width="15" height="12" viewBox="0 0 24 18"><rect x="0" y="0" width="24" height="18" fill="#fff"/><path d="M1 1l11 9 11-9" fill="none" stroke="#f07c2a" stroke-width="2"/></svg>
      </span>
    </div>
    <div class="tagline">WE ARE A FUN ENVIRONMENT</div>
  </div>
</section>

<section class="card card-back">
  <div class="heart-decor" role="img" aria-label="Two faint overlapping hearts"></div>
  <div class="back-content">
    <div class="brand-name">MARGARET'S</div>
    <div class="brand-sub">FAMILY SOBER HOUSE INC.</div>
    <div class="back-tagline">WE ARE A FUN ENVIRONMENT</div>
    <div class="back-address">XXX Some Street Address, Arizona, USA</div>
  </div>
</section>

</body>
</html>
```